2021 Summer Ads Danford Vale Custom Homes

We need a re-design of our summer ad run for our customer, Danford Vale Custom Homes. They are custom home builders in the mostly rural parts of West Virginia, USA. They are known for their "Forever Home" tagline. We'd like two designed ads with the main difference being just the custom home that's featured. These designs should be for a Google banner like 300 x 250 and square ad like 250 x 250. For inspiration please visit the Danford Vale Custom Homes website at www dot danfordvalecustomhomes dot com

Target Market(s)

consumers / new home shoppers

Industry/Entity Type

Consumer

Requirements
Must have
• DVCH logo
Price Lock Available!
Custom home pic
Learn more >
small TBWG logo mark

```html
<!DOCTYPE html>
<html lang="en">
<head>
<meta charset="utf-8">
<title>DVCH Banner-1</title>
<link href="https://fonts.googleapis.com/css2?family=Montserrat:wght@300;400;600;700;800&display=swap" rel="stylesheet">
<style>
  :root {
    --board-light: #b4b4b4;
    --board-dark: #767676;
    --navy: #121d47;
    --navy-deep: #0c1536;
    --navy-soft: #1d2c5e;
    --brand-red: #d40f14;
    --brand-red-dark: #a20c10;
    --white: #ffffff;
    --logo-ink: #8c1216;
    --photo-sky: #9fb6c9;
    --photo-trees: #4f7a3a;
    --photo-barn: #a5321f;
    --photo-ground: #8b8579;
  }
  * { margin: 0; padding: 0; box-sizing: border-box; }
  html, body { width: 900px; height: 1200px; overflow: hidden; }
  body {
    position: relative;
    font-family: "Montserrat", Arial, sans-serif;
    background: radial-gradient(ellipse at 50% 45%, var(--board-light) 0%, #9a9a9a 55%, var(--board-dark) 100%);
    color: var(--white);
  }
  .board-title {
    position: absolute; top: 74px; left: 0; width: 900px;
    text-align: center; font-weight: 700; font-size: 24px; letter-spacing: 0.5px;
  }
  .size-label {
    position: absolute; left: 0; width: 900px;
    text-align: center; font-weight: 400; font-size: 24px; letter-spacing: 0.5px;
  }
  .size-label--wide { top: 176px; }
  .size-label--square { top: 670px; }
  .banner {
    position: absolute; display: block;
    box-shadow: 0 8px 22px rgba(0,0,0,0.28);
  }
  .banner--wide { left: 229.5px; top: 231px; width: 450px; height: 375px; }
  .banner--square { left: 267px; top: 727.5px; width: 375px; height: 375px; }
  .headline { font-family: "Montserrat", Arial, sans-serif; font-weight: 800; fill: var(--white); }
  .tag-text { font-family: "Montserrat", Arial, sans-serif; font-weight: 700; fill: var(--navy); }
  .cta-text { font-family: "Montserrat", Arial, sans-serif; font-weight: 700; fill: var(--white); }
  .logo-text { font-family: "Montserrat", Arial, sans-serif; font-weight: 800; fill: var(--logo-ink); }
  .badge-text { font-family: "Montserrat", Arial, sans-serif; font-weight: 700; fill: var(--white); }
</style>
</head>
<body>
  <h1 class="board-title">DVCH BANNER-1</h1>

  <p class="size-label size-label--wide">300X250</p>
  <svg class="banner banner--wide" viewBox="0 0 300 250" xmlns="http://www.w3.org/2000/svg">
    <defs>
      <linearGradient id="navyWide" x1="0" y1="0" x2="1" y2="1">
        <stop offset="0" stop-color="var(--navy-soft)"/>
        <stop offset="0.5" stop-color="var(--navy)"/>
        <stop offset="1" stop-color="var(--navy-deep)"/>
      </linearGradient>
      <linearGradient id="photoWide" x1="0" y1="0" x2="0" y2="1">
        <stop offset="0" stop-color="var(--photo-sky)"/>
        <stop offset="0.22" stop-color="var(--photo-trees)"/>
        <stop offset="0.5" stop-color="var(--photo-barn)"/>
        <stop offset="0.75" stop-color="var(--photo-barn)"/>
        <stop offset="1" stop-color="var(--photo-ground)"/>
      </linearGradient>
    </defs>
    <rect class="banner-bg" width="300" height="250" fill="url(#navyWide)"/>
    <polygon points="150,0 300,0 300,90" fill="var(--navy-soft)" opacity="0.45"/>
    <polygon points="140,250 300,140 300,250" fill="var(--navy-deep)" opacity="0.6"/>
    <path class="photo" role="img" aria-label="Photo of a red custom-built barn house with a grey roof, surrounded by green trees"
      d="M0,0 H72 C105,45 142,95 136,140 C132,170 112,188 88,192 L0,196 Z" fill="url(#photoWide)"/>
    <path class="accent-band" d="M76,0 C110,45 146,96 140,140 C136,172 114,190 88,194"
      fill="none" stroke="var(--brand-red)" stroke-width="6"/>
    <path class="logo-field" d="M0,196 C40,172 112,176 130,205 C138,220 134,240 134,250 H0 Z" fill="var(--white)"/>
    <text class="logo-text" x="62" y="223" font-size="11.5" text-anchor="middle">DANFORD VALE</text>
    <text class="logo-text" x="62" y="235" font-size="6.5" text-anchor="middle">CUSTOM HOMES</text>

    <text class="headline" x="223" y="69" font-size="41" text-anchor="middle">PRICE</text>
    <text class="headline" x="223" y="104" font-size="41" text-anchor="middle">LOCK</text>
    <rect class="tag" x="164" y="111" width="116" height="22" fill="var(--white)"/>
    <text class="tag-text" x="222" y="127.5" font-size="14.5" text-anchor="middle">AVAILABLE!</text>

    <rect class="cta" x="165" y="144" width="117" height="32" rx="4" fill="var(--brand-red)"/>
    <text class="cta-text" x="213" y="164.5" font-size="11.5" text-anchor="middle">LEARN MORE</text>
    <circle cx="266" cy="160.5" r="7" fill="var(--white)"/>
    <path d="M264,156.5 L268,160.5 L264,164.5" fill="none" stroke="var(--brand-red)" stroke-width="2" stroke-linecap="round" stroke-linejoin="round"/>

    <text class="badge-text" x="219" y="219" font-size="14" text-anchor="middle">TBWG</text>
    <text class="badge-text" x="219" y="227" font-size="4.5" text-anchor="middle">Timber Builders</text>
    <text class="badge-text" x="219" y="232.5" font-size="4.5" text-anchor="middle">Working Group</text>
  </svg>

  <p class="size-label size-label--square">250X250</p>
  <svg class="banner banner--square" viewBox="0 0 250 250" xmlns="http://www.w3.org/2000/svg">
    <defs>
      <linearGradient id="navySquare" x1="0" y1="0" x2="1" y2="1">
        <stop offset="0" stop-color="var(--navy-soft)"/>
        <stop offset="0.5" stop-color="var(--navy)"/>
        <stop offset="1" stop-color="var(--navy-deep)"/>
      </linearGradient>
      <linearGradient id="photoSquare" x1="0" y1="0" x2="0" y2="1">
        <stop offset="0" stop-color="var(--photo-sky)"/>
        <stop offset="0.22" stop-color="var(--photo-trees)"/>
        <stop offset="0.5" stop-color="var(--photo-barn)"/>
        <stop offset="0.75" stop-color="var(--photo-barn)"/>
        <stop offset="1" stop-color="var(--photo-ground)"/>
      </linearGradient>
    </defs>
    <rect class="banner-bg" width="250" height="250" fill="url(#navySquare)"/>
    <polygon points="110,0 250,0 250,80" fill="var(--navy-soft)" opacity="0.45"/>
    <polygon points="115,250 250,150 250,250" fill="var(--navy-deep)" opacity="0.6"/>
    <path class="photo" role="img" aria-label="Photo of a red custom-built barn house with a grey roof, surrounded by green trees"
      d="M0,0 H30 C70,45 118,100 112,145 C108,175 90,190 70,194 L0,198 Z" fill="url(#photoSquare)"/>
    <path class="accent-band" d="M34,0 C74,45 122,100 116,145 C112,177 92,192 70,196"
      fill="none" stroke="var(--brand-red)" stroke-width="6"/>
    <path class="logo-field" d="M0,198 C35,176 96,178 112,205 C119,220 116,240 116,250 H0 Z" fill="var(--white)"/>
    <text class="logo-text" x="56" y="225" font-size="10.5" text-anchor="middle">DANFORD VALE</text>
    <text class="logo-text" x="56" y="236" font-size="6" text-anchor="middle">CUSTOM HOMES</text>

    <text class="headline" x="182" y="83" font-size="36" text-anchor="middle">PRICE</text>
    <text class="headline" x="182" y="113" font-size="36" text-anchor="middle">LOCK</text>
    <rect class="tag" x="132" y="116" width="100" height="21" fill="var(--white)"/>
    <text class="tag-text" x="182" y="131.5" font-size="12.5" text-anchor="middle">AVAILABLE!</text>

    <rect class="cta" x="134" y="147" width="98" height="28" rx="4" fill="var(--brand-red)"/>
    <text class="cta-text" x="174" y="165" font-size="10" text-anchor="middle">LEARN MORE</text>
    <circle cx="219" cy="161" r="6" fill="var(--white)"/>
    <path d="M217.3,157.5 L220.7,161 L217.3,164.5" fill="none" stroke="var(--brand-red)" stroke-width="1.8" stroke-linecap="round" stroke-linejoin="round"/>

    <text class="badge-text" x="184" y="222" font-size="12" text-anchor="middle">TBWG</text>
    <text class="badge-text" x="184" y="229" font-size="4" text-anchor="middle">Timber Builders</text>
    <text class="badge-text" x="184" y="234" font-size="4" text-anchor="middle">Working Group</text>
  </svg>
</body>
</html>
```